Chartered accountants trying to make boring information more appealing!

We are UK based chartered accountants with various specialist areas of expertise. We need a template for a monthly mailer that we send to our clients and contacts to keep them updated with key financial news. The update is called Tin Lantern and we'd like it to fit on one page of A4 that we can then drop text into. We would like it to be more appealing than just the usual calculators and audit papers associated with accountants. Our brand colours are blue and green.

Target Market(s)

Our clients range from small businesses to large pension fund trustees, charities and individuals. It must appeal to everyone.

Industry/Entity Type

Accounting

Colors
34a7d8
33b8a4
3277b5

Requirements
Must have
• Space for text. The title 'Tin Lantern'. Our logo.
Nice to have
• Sky's the limit!
Should not have
• Shouldn't look homemade. I've attached an old one done in house - please avoid this!

```html
<!DOCTYPE html>
<html lang="en">
<head>
<meta charset="utf-8">
<title>Tin Lantern Alert – March 2016</title>
<link rel="stylesheet" href="https://fonts.googleapis.com/css2?family=Oswald:wght@500;700&family=Lato:wght@400;700&family=Roboto:wght@400;500&display=swap">
<style>
:root{
  --sky:#34a7d8;
  --teal:#33b8a4;
  --blue:#3277b5;
  --navy:#1f4f8a;
  --ink:#1c1c1c;
  --body:#2a2a2a;
  --paper:#ffffff;
  --stage:#d9dbde;
  --mint:#2fe0c8;
}
*{margin:0;padding:0;box-sizing:border-box}
html,body{width:900px;height:1200px;overflow:hidden;background:var(--stage)}
.canvas{position:relative;width:900px;height:1200px}
.mailer{position:absolute;left:72px;top:48px;width:756px;height:1084px;background:var(--paper);overflow:hidden;
  box-shadow:0 4px 14px rgba(0,0,0,.25)}
.mailer > *{position:absolute}
.brand{left:52px;top:52px;font-family:"Lato",sans-serif;font-weight:400;font-size:44px;color:var(--blue);letter-spacing:-.5px}
.brand-sub{left:56px;top:104px;font-family:"Lato",sans-serif;font-size:8.5px;letter-spacing:1.5px;color:var(--blue)}
.hero-photo{right:0;top:20px;width:470px;height:372px;background:linear-gradient(135deg,#f4f5f7 0%,#d7dbe2 35%,#2a3342 60%,#1b2230 100%);
  clip-path:polygon(14% 0,100% 0,100% 100%,40% 100%,0 38%)}
.title-band{left:0;top:147px;width:470px;height:170px;background:linear-gradient(100deg,var(--sky) 0%,#33bcc4 45%,var(--teal) 100%);
  clip-path:polygon(0 0,88% 0,100% 50%,88% 100%,0 100%)}
.title-alert{left:16px;top:168px;font-family:"Oswald",sans-serif;font-weight:700;font-size:38px;color:var(--ink);line-height:1;transform:scaleX(.95);transform-origin:left}
.title-month{left:16px;top:212px;font-family:"Roboto",sans-serif;font-size:40px;color:#fff;line-height:1}
.title-theme{left:20px;top:266px;font-family:"Roboto",sans-serif;font-size:34px;color:var(--ink);line-height:1}
.tagline-band{left:0;top:320px;width:470px;height:74px;background:linear-gradient(90deg,var(--blue),#3a8ad0);
  clip-path:polygon(0 0,94% 0,100% 100%,0 100%)}
.tagline{left:18px;top:328px;font-family:"Roboto",sans-serif;font-size:25px;line-height:32px;color:#fff}
.rule{left:0;top:396px;width:756px;height:3px;background:var(--blue)}
.lead{left:16px;top:418px;width:424px;font-family:"Lato",sans-serif;font-weight:700;font-size:14px;line-height:18px;color:var(--ink);text-align:justify}
.section-tag{left:0;height:36px;background:linear-gradient(90deg,var(--blue),var(--sky));color:#fff;font-family:"Oswald",sans-serif;font-weight:500;
  font-size:20px;line-height:36px;padding-left:18px;clip-path:polygon(0 0,100% 0,94% 100%,0 100%)}
.section-text{left:16px;width:424px;font-family:"Lato",sans-serif;font-size:13px;line-height:16px;color:var(--body);text-align:justify}
.section-text b{font-weight:700}
.action-panel{left:463px;top:407px;width:293px;height:677px;background:var(--blue)}
.action-head{left:463px;top:407px;width:293px;height:68px;padding:8px 18px;font-family:"Oswald",sans-serif;font-weight:500;font-size:18px;line-height:24px;
  color:#fff;background:#2f6fae;border-bottom:2px solid #fff;letter-spacing:.3px}
.action-list{left:480px;top:486px;width:260px;list-style:none;font-family:"Lato",sans-serif;font-weight:700;font-size:14px;line-height:18px;color:#fff}
.action-list li{position:relative;padding-left:15px;margin-bottom:18px}
.action-list li::before{content:"";position:absolute;left:0;top:5px;width:7px;height:7px;border-radius:50%;background:var(--mint)}
.action-note{left:481px;top:693px;width:255px;font-family:"Lato",sans-serif;font-size:14px;line-height:18px;color:#fff;text-align:justify}
.link-bar{left:463px;top:854px;width:293px;height:19px;background:var(--mint);font-family:"Lato",sans-serif;font-weight:700;font-size:13.5px;line-height:19px;color:var(--ink);padding-left:18px}
.panel-photo{left:481px;top:888px;width:253px;height:104px;border:2px solid #fff;background:linear-gradient(120deg,#eef2f6,#b9c6d4 55%,#7f95ab)}
.contact-band{left:463px;top:1008px;width:293px;height:60px;background:linear-gradient(90deg,#2f6fae,var(--teal));font-family:"Lato",sans-serif;font-size:13px;color:#fff}
.contact-band span{position:absolute;display:flex;align-items:center;gap:4px}
.contact-band svg{width:9px;height:9px;fill:#fff}
.foot-bar{left:0;top:1068px;width:756px;height:16px;background:var(--blue)}
</style>
</head>
<body>
<div class="canvas">
  <article class="mailer">
    <div class="brand">Harwell</div>
    <div class="brand-sub">CHARTERED ACCOUNTANTS</div>

    <div class="hero-photo" role="img" aria-label="Photo of a businessman in a suit drawing a rising bar chart with an upward arrow on a glass board"></div>

    <div class="title-band"></div>
    <h1 class="title-alert">TIN LANTERN ALERT</h1>
    <div class="title-month">MARCH 2016</div>
    <div class="title-theme">SKY IS THE LIMIT</div>

    <div class="tagline-band"></div>
    <p class="tagline">Keeping you up to date<br>with the latest accounting news</p>
    <div class="rule"></div>

    <p class="lead">Welcome to Harwell Tin Lantern. This issue covers the new National Living Wage, PAYE Settlement Agreements and the latest news on pension contributions due to be announced in the Budget.</p>

    <h2 class="section-tag" style="top:502px;width:425px">The new National Living Wage (“NLW”)</h2>
    <p class="section-text" style="top:554px">From <b>April 2016,</b> the Government’s new National Living Wage will become law. This means that all workers aged 25 and over are legally entitled to be paid at least <b>£7.20</b> per hour. If you’re an employer, you will need to make sure that you are paying your staff correctly from <b>1st April</b>, as the National Living Wage will be enforced just as strongly as the current National Minimum Wage.</p>

    <h2 class="section-tag" style="top:663px;width:407px">PAYE Settlement Agreements (“PSA”)</h2>
    <p class="section-text" style="top:723px">A PSA allows an employer to make one annual payment to cover all the tax and National Insurance due on small or irregular taxable benefits or expenses. This can be beneficial as it avoids the need to include these on annual P11D forms, or to calculate and charge tax and National Insurance on such items through the payroll.</p>

    <h2 class="section-tag" style="top:810px;width:222px">What is covered?</h2>
    <p class="section-text" style="top:862px;font-size:13.5px;line-height:17px">A PSA is intended to cover items that are minor irregular gifts, such as a small birthday present, gift voucher, staff entertaining or one off relocation expenses. It can also include items where it would be impracticable to either operate PAYE on the amount, or difficult to identify with a shared benefit, how much relates to each employee in order to report it on a form P11D, e.g. the cost of a staff Christmas party, that doesn’t qualify for relief. A PSA cannot be used for items such as bonuses, round sum allowances, beneficial loans or more high-value benefits such as company cars. If you apply after the start of the tax year, there are some restrictions on what you can include.</p>

    <div class="action-panel"></div>
    <h3 class="action-head">To make sure that you are readyfor the change, you must:</h3>
    <ul class="action-list">
      <li>Check which of your employees is eligible to receive the NLW</li>
      <li>Take the appropriate payroll actions</li>
      <li>Let your staff know about their new pay rates</li>
      <li>Check that your staff under 25 are earning at least the right rate of National Minimum Wage</li>
    </ul>
    <p class="action-note">If you’re concerned about the effects of the new National Living Wage or would like some help to implement the changes, why not call one of our Payroll experts on 0116 496 0123 for some specialist advice? You can find out more about the National Living Wage, including new rates of pay on the Government website at</p>
    <div class="link-bar">www.wagefacts.org/national-minimum-wage</div>
    <div class="panel-photo" role="img" aria-label="Photo of hands working with a tablet over printed financial charts"></div>

    <div class="contact-band">
      <span style="left:10px;top:10px"><svg viewBox="0 0 10 10"><path d="M2 0l2 2-1 1.5c.8 1.6 2 2.8 3.5 3.5L8 6l2 2-1.5 2C4.5 9.6.4 5.5 0 1.5z"/></svg>44 (0)116 496 0123</span>
      <span style="left:148px;top:10px"><svg viewBox="0 0 10 10"><rect x="0" y="1.5" width="10" height="7" rx="1"/></svg>post@harwellca.biz</span>
      <span style="left:10px;top:32px"><svg viewBox="0 0 10 10"><circle cx="5" cy="5" r="4.5"/></svg>www.harwellca.biz</span>
    </div>
    <div class="foot-bar"></div>
  </article>
</div>
</body>
</html>
```